Orthodontist Needs Promotional Discount Postcard

5.5 x 8.5 Horizontal 2-Sided Postcard for mailing.
Images & Logo on both sides okay; must be free stock Images from legit sources only, or use attached images. See our website for information, CoveLineSmiles.com
Context to include:
New Patient Special $500 off Braces or Clear Aligners
Cannot be combined with any other discounts.
Major dental insurance plans and Vita-Plan accepted
Affordable payment options are available
Call to schedule your free consultation
Present this new patient offer to receive your discount.
Offer ends January 31, 2022.
805-419-2276 www. CoveLineSmiles.com
462 N. Marigold Street, Suite B, Ventura, CA 93001-5812
office@covelinesmiles.com

```html
<!DOCTYPE html>
<html lang="en">
<head>
<meta charset="utf-8">
<title>Cove Line Smiles – New Patient Postcard</title>
<link href="https://fonts.googleapis.com/css2?family=Roboto:ital,wght@0,400;0,500;0,700;0,900;1,700&family=Roboto+Condensed:wght@700&family=Yellowtail&display=swap" rel="stylesheet">
<style>
  :root{
    --stage:#777879;
    --blue:#3db5e6;
    --blue-light:#a9dcf2;
    --slate:#4b555d;
    --slate-dark:#3a4249;
    --ink:#262b30;
    --grey-text:#5b656c;
    --red:#e8302f;
    --paper:#eeeff0;
    --white:#ffffff;
  }
  *{margin:0;padding:0;box-sizing:border-box}
  html,body{width:876px;height:1200px;overflow:hidden;background:var(--stage);font-family:"Roboto",sans-serif}
  .postcard{position:absolute;left:36px;width:805px;height:508px;overflow:hidden;box-shadow:0 14px 18px rgba(0,0,0,.28)}
  .front{top:48px;background:var(--white)}
  .back{top:623px;background:var(--paper)}
  .abs{position:absolute}

  .brand{position:absolute;display:flex;align-items:center;gap:12px}
  .brand-dot{border-radius:50%;background:var(--blue)}
  .brand-name{font-family:"Roboto",sans-serif;font-weight:500;color:var(--blue);letter-spacing:.5px;white-space:nowrap}
  .front .brand{left:28px;top:22px}
  .front .brand-dot{width:89px;height:89px}
  .front .brand-name{font-size:28px}
  .back .brand{left:27px;top:44px;gap:9px}
  .back .brand-dot{width:53px;height:53px}
  .back .brand-name{font-size:20px}

  .headline{left:27px;top:128px;font-weight:900;font-size:44px;color:var(--ink);letter-spacing:-.5px}
  .offer-line{left:72px;top:172px;display:flex;align-items:baseline;gap:4px}
  .offer-script{font-family:"Yellowtail",cursive;color:var(--red);font-size:40px}
  .offer-amount{font-weight:900;color:var(--blue);font-size:45px;letter-spacing:-.5px}
  .subhead{left:29px;top:220px;font-weight:700;font-size:31px;color:var(--grey-text);letter-spacing:-.3px}

  .hero-photo{left:395px;top:0;width:410px;height:300px;background:linear-gradient(135deg,#f2f2f2 0%,#8a6a55 45%,#2d2a2a 75%,#d8d8d8 100%)}

  .feature{position:absolute;top:274px;width:241px;height:139px;background:var(--white);border-radius:5px;box-shadow:0 2px 6px rgba(0,0,0,.18);text-align:center}
  .feature svg{margin-top:20px}
  .feature p{position:absolute;left:0;right:0;top:82px;font-weight:700;font-size:16.5px;line-height:19px;color:var(--slate)}

  .cta-bar{left:0;top:440px;width:461px;height:44px;background:var(--blue);display:flex;align-items:center;padding-left:28px}
  .cta-bar span{font-weight:700;font-style:italic;font-size:18px;color:var(--white);letter-spacing:.2px;white-space:nowrap}
  .contact-phone{left:519px;top:423px;font-weight:900;font-size:38px;color:var(--white);letter-spacing:.5px}
  .contact-web{left:519px;top:460px;font-weight:700;font-size:27px;color:var(--white)}
  .contact-icon{left:476px}

  .smile-braces{left:46px;top:138px;width:172px;height:172px;border-radius:50%;background:radial-gradient(circle at 50% 50%,#f4f1ec 0%,#d77a7c 55%,#b2585e 100%);box-shadow:0 0 0 8px var(--blue-light)}
  .smile-aligner{left:199px;top:142px;width:260px;height:260px;border-radius:50%;background:radial-gradient(circle at 50% 52%,#f7f5f2 0%,#e4a39b 50%,#efc9bc 100%);box-shadow:0 0 0 9px var(--blue-light)}

  .contact-title{left:29px;top:352px;font-weight:700;font-size:20px;color:var(--white)}
  .contact-list{left:28px;top:381px;list-style:none;color:var(--white);font-size:14px;line-height:17px}
  .contact-list li{display:flex;gap:8px;align-items:flex-start;margin-bottom:6px}
  .contact-list svg{flex:none;margin-top:2px}

  .postage{left:686px;top:51px;width:88px;height:84px;border:1.5px solid var(--slate-dark);color:var(--red);font-weight:700;font-size:9.5px;line-height:12.5px;text-align:center;padding-top:9px}
  .postage strong{font-size:12px}
  .mail-block{left:581px;top:226px;width:193px;height:101px;border:1px solid var(--slate);padding:10px 12px;color:var(--ink);font-weight:700;font-size:15px}
  .mail-block .route{font-size:14px;letter-spacing:.3px;margin-bottom:20px}
  .disclaimer{right:31px;top:432px;font-family:"Roboto Condensed",sans-serif;font-weight:700;font-variant:small-caps;font-size:12px;color:var(--ink);white-space:nowrap}
  .offer-ends{left:481px;top:446px;width:293px;height:29px;background:var(--blue);color:var(--white);font-weight:700;font-size:19px;display:flex;align-items:center;justify-content:center;white-space:nowrap}
</style>
</head>
<body>

<section class="postcard front">
  <svg class="abs" style="left:0;top:0" width="805" height="508" viewBox="0 0 805 508">
    <defs>
      <linearGradient id="bandFade" x1="0" y1="0" x2="0" y2="1">
        <stop offset="0" stop-color="#6e7880"/>
        <stop offset="1" stop-color="#3a4249"/>
      </linearGradient>
    </defs>
    <path d="M0 305 C180 372 470 330 560 290 C650 250 740 250 805 310 L805 508 L0 508 Z" fill="url(#bandFade)"/>
    <path d="M0 298 C180 366 470 322 560 282 C650 242 740 242 805 302" fill="none" stroke="var(--blue)" stroke-width="6"/>
  </svg>

  <div class="abs hero-photo" role="img" aria-label="Photo of a smiling father with his son and daughter, the daughter wearing braces"></div>
  <svg class="abs" style="left:395px;top:250px" width="410" height="70" viewBox="0 0 410 70">
    <path d="M0 70 L0 40 C60 20 140 -2 230 12 C300 22 360 40 410 62 L410 70 Z" fill="#6a747c"/>
    <path d="M0 40 C60 20 140 -2 230 12 C300 22 360 40 410 62" fill="none" stroke="var(--blue)" stroke-width="6"/>
  </svg>

  <div class="brand"><span class="brand-dot"></span><span class="brand-name">COVE LINE SMILES</span></div>

  <h1 class="abs headline">New Patient</h1>
  <div class="abs offer-line"><span class="offer-script">Special</span><span class="offer-amount">$500 OFF</span></div>
  <h2 class="abs subhead">Braces or Clear Aligners</h2>

  <div class="feature" style="left:28px">
    <svg width="56" height="52" viewBox="0 0 56 52" aria-hidden="true">
      <rect x="14" y="2" width="40" height="28" rx="4" fill="var(--blue)" transform="rotate(-14 34 16)" opacity=".75"/>
      <rect x="2" y="14" width="44" height="34" rx="4" fill="var(--blue)"/>
      <rect x="8" y="22" width="14" height="8" rx="1" fill="var(--white)"/>
      <rect x="8" y="36" width="8" height="3" fill="var(--white)"/><rect x="19" y="36" width="8" height="3" fill="var(--white)"/><rect x="30" y="36" width="8" height="3" fill="var(--white)"/>
    </svg>
    <p>Affordable payment<br>options available</p>
  </div>
  <div class="feature" style="left:282px">
    <svg width="56" height="56" viewBox="0 0 56 56" aria-hidden="true">
      <path d="M4 2 H28 L36 10 V50 H4 Z" fill="var(--blue)"/>
      <rect x="10" y="16" width="16" height="3" fill="var(--white)"/><rect x="10" y="24" width="20" height="3" fill="var(--white)"/><rect x="10" y="32" width="14" height="3" fill="var(--white)"/>
      <path d="M30 26 C36 22 42 26 44 26 C46 26 52 22 54 28 C56 34 52 40 50 46 C49 52 46 54 45 48 C44 42 42 40 40 46 C39 52 36 54 35 48 C34 40 28 34 30 26 Z" fill="var(--blue)" stroke="var(--white)" stroke-width="2"/>
    </svg>
    <p>Vita-Plan Dental and major<br>insurance plans accepted</p>
  </div>
  <div class="feature" style="left:536px">
    <svg width="56" height="56" viewBox="0 0 56 56" aria-hidden="true">
      <path d="M8 26 C8 10 20 2 32 4 C40 6 44 12 42 20 L46 28 L42 30 V38 C42 42 38 42 34 42 V52 H14 V40 C10 36 8 32 8 26 Z" fill="var(--blue)"/>
      <rect x="48" y="20" width="6" height="2.5" fill="var(--blue)"/><rect x="48" y="26" width="7" height="2.5" fill="var(--blue)"/><rect x="48" y="32" width="6" height="2.5" fill="var(--blue)"/>
    </svg>
    <p>Hablamos Español</p>
  </div>

  <div class="abs cta-bar"><span>CALL TO SCHEDULE YOUR FREE CONSULTATION !</span></div>
  <svg class="abs contact-icon" style="top:434px" width="22" height="22" viewBox="0 0 24 24" aria-hidden="true"><path d="M6.6 10.8a15 15 0 0 0 6.6 6.6l2.2-2.2c.3-.3.7-.4 1-.2 1.1.4 2.3.6 3.6.6.6 0 1 .4 1 1V20c0 .6-.4 1-1 1A17 17 0 0 1 3 4c0-.6.4-1 1-1h3.5c.6 0 1 .4 1 1 0 1.3.2 2.5.6 3.6.1.3 0 .7-.2 1z" fill="var(--blue)"/></svg>
  <svg class="abs contact-icon" style="top:465px" width="22" height="22" viewBox="0 0 24 24" aria-hidden="true"><circle cx="12" cy="12" r="10" fill="none" stroke="var(--blue)" stroke-width="2"/><ellipse cx="12" cy="12" rx="4.5" ry="10" fill="none" stroke="var(--blue)" stroke-width="2"/><path d="M2 12h20M4 7h16M4 17h16" stroke="var(--blue)" stroke-width="1.6"/></svg>
  <div class="abs contact-phone">805-419-2276</div>
  <div class="abs contact-web">CoveLineSmiles.com</div>
</section>

<section class="postcard back">
  <svg class="abs" style="left:0;top:0" width="805" height="508" viewBox="0 0 805 508">
    <path d="M0 207 C90 170 180 180 240 220 C330 280 380 360 362 508 L0 508 Z" fill="var(--blue)"/>
    <path d="M0 200 C90 162 180 172 244 214 C336 276 388 360 370 508" fill="none" stroke="var(--slate)" stroke-width="1.5"/>
  </svg>

  <div class="brand"><span class="brand-dot"></span><span class="brand-name">COVE LINE SMILES</span></div>

  <div class="abs smile-braces" role="img" aria-label="Close-up photo of a smile with metal braces"></div>
  <div class="abs smile-aligner" role="img" aria-label="Close-up photo of a hand fitting a clear aligner onto teeth"></div>

  <h3 class="abs contact-title">Contact Us</h3>
  <ul class="abs contact-list">
    <li><svg width="12" height="14" viewBox="0 0 12 14" aria-hidden="true"><path d="M6 1a4 4 0 0 1 4 4c0 3-4 8-4 8S2 8 2 5a4 4 0 0 1 4-4z" fill="none" stroke="var(--white)" stroke-width="1.4"/><circle cx="6" cy="5" r="1.4" fill="var(--white)"/></svg><span>462 N Marigold St, Suite B<br>Ventura, CA 93001</span></li>
    <li><svg width="12" height="12" viewBox="0 0 12 12" aria-hidden="true"><circle cx="6" cy="6" r="5.2" fill="none" stroke="var(--white)" stroke-width="1.2"/><path d="M4 3.5l1 1.8-.6.7a4 4 0 0 0 1.8 1.8l.7-.6 1.7 1-.6 1c-2.7 0-5-2.3-5-5z" fill="var(--white)"/></svg><span>805-419-2276</span></li>
    <li><svg width="12" height="12" viewBox="0 0 12 12" aria-hidden="true"><rect x="1" y="3" width="10" height="7" fill="none" stroke="var(--white)" stroke-width="1.2"/><path d="M1 3l5 4 5-4" fill="none" stroke="var(--white)" stroke-width="1.2"/></svg><span>office@covelinesmiles.com</span></li>
    <li><svg width="12" height="12" viewBox="0 0 12 12" aria-hidden="true"><circle cx="6" cy="6" r="5.2" fill="none" stroke="var(--white)" stroke-width="1.2"/><ellipse cx="6" cy="6" rx="2.3" ry="5.2" fill="none" stroke="var(--white)" stroke-width="1"/><path d="M1 6h10" stroke="var(--white)" stroke-width="1"/></svg><span>CoveLineSmiles.com</span></li>
  </ul>

  <div class="abs postage">Standard<br>U.S.POSTAGE<br><strong>PAID</strong><br>Post Relay,<br>Inc.</div>
  <div class="abs mail-block"><div class="route">**********ECRWSS****</div>Local<br>Postal Customer</div>

  <div class="abs disclaimer">Present this offer to receive discount. Cannot combine with any other offer</div>
  <div class="abs offer-ends">Offer ends January 31, 2022</div>
</section>

</body>
</html>
```